wood grain ultrasonic essential oil aroma diffuser

Design a package that is simple but luxurious for the diffuser with my logo. My business is called “Kindle the Moss”. The logo incorporates “Thoughts become things” the concept is positive thinking. I don’t particularly want the product featured as I have like to develop a uniform look for packaging and website and there are 2 different diffusers,

Target Market(s)

People interested in yoga, meditation, metaphysical aspects

Industry/Entity Type

Health And Wellness

Colors

Designer to choose colors to be used in the design.

Requirements
Must have
• Luxurious feel to packaging and alignment with the website

```html
<!DOCTYPE html>
<html lang="en">
<head>
<meta charset="utf-8">
<title>Kindle the Moss – Diffuser Carton Dieline</title>
<link rel="stylesheet" href="https://fonts.googleapis.com/css2?family=Jost:wght@400;500&display=swap">
<style>
  :root {
    --paper: #ffffff;
    --pattern-cream: #f1e9db;
    --pattern-line: #e4d5b8;
    --gold-light: #e3c48e;
    --gold-dark: #b88a4a;
    --rule-gold: #c29a5e;
    --ink: #1e1a17;
    --wood-light: #e8953a;
    --wood-mid: #d8731e;
    --wood-dark: #b0480f;
    --cut-line: #f0c4c4;
  }
  html, body {
    margin: 0;
    width: 859px;
    height: 1200px;
    overflow: hidden;
    background: var(--paper);
  }
  .dieline {
    position: absolute;
    left: 0;
    top: 270px;
    width: 859px;
    height: 660px;
  }
  .cut { fill: none; stroke: var(--cut-line); stroke-width: 1.2; }
  .pattern-field { fill: var(--pattern-cream); }
  .white-band { fill: var(--paper); }
  .brand-name {
    font-family: 'Jost', sans-serif;
    font-weight: 400;
    font-size: 11px;
    text-anchor: middle;
  }
  .brand-name--ink { fill: var(--ink); }
  .brand-name--light { fill: #ffffff; }
  .brand-dot--ink { fill: var(--ink); }
  .brand-dot--light { fill: none; stroke: #ffffff; stroke-width: 1.5; }
  .product-title {
    font-family: 'Jost', sans-serif;
    font-weight: 500;
    font-size: 12px;
    fill: var(--ink);
    text-anchor: middle;
  }
  .gold-rule { stroke: var(--rule-gold); stroke-width: 2.5; }
</style>
</head>
<body>
<svg class="dieline" viewBox="0 690 1070 822" xmlns="http://www.w3.org/2000/svg">
  <defs>
    <linearGradient id="gold-plate" x1="0" y1="0" x2="1" y2="1">
      <stop offset="0" stop-color="var(--gold-dark)"/>
      <stop offset="0.5" stop-color="var(--gold-light)"/>
      <stop offset="1" stop-color="var(--gold-dark)"/>
    </linearGradient>
    <linearGradient id="wood-a" x1="0" y1="0" x2="1" y2="0">
      <stop offset="0" stop-color="var(--wood-mid)"/>
      <stop offset="0.2" stop-color="var(--wood-light)"/>
      <stop offset="0.36" stop-color="var(--wood-dark)"/>
      <stop offset="0.5" stop-color="var(--wood-light)"/>
      <stop offset="0.7" stop-color="var(--wood-mid)"/>
      <stop offset="0.85" stop-color="var(--wood-light)"/>
      <stop offset="1" stop-color="var(--wood-mid)"/>
    </linearGradient>
    <linearGradient id="wood-b" x1="0" y1="0" x2="1" y2="0">
      <stop offset="0" stop-color="var(--wood-dark)"/>
      <stop offset="0.25" stop-color="var(--wood-mid)"/>
      <stop offset="0.45" stop-color="var(--wood-light)"/>
      <stop offset="0.65" stop-color="var(--wood-dark)"/>
      <stop offset="0.85" stop-color="var(--wood-light)"/>
      <stop offset="1" stop-color="var(--wood-mid)"/>
    </linearGradient>
    <radialGradient id="diffuser-tone" cx="0.45" cy="0.55" r="0.6">
      <stop offset="0" stop-color="#f2c27a"/>
      <stop offset="0.7" stop-color="#d9953f"/>
      <stop offset="1" stop-color="#b8752c"/>
    </radialGradient>
  </defs>

  <!-- cut and fold outlines -->
  <path class="cut" d="M45,990 L15,998 V1334 L45,1342"/>
  <path class="cut" d="M300,983 V865 H518 L550,912 V983"/>
  <path class="cut" d="M800,983 L835,865 H1040 L1050,880 V983"/>
  <path class="cut" d="M45,1347 V1500 H108 V1468 H240 V1500 H298 V1347"/>
  <path class="cut" d="M300,1347 V1400 L425,1460 H550 V1347"/>
  <path class="cut" d="M550,1347 L612,1500 H740 L800,1347"/>
  <path class="cut" d="M800,1347 V1460 H925 L1050,1400 V1347"/>

  <!-- lid panel -->
  <g class="lid-panel">
    <rect class="pattern-field" x="45" y="700" width="255" height="285" role="img" aria-label="Cream geometric line pattern"/>
    <rect x="122" y="808" width="100" height="94" fill="url(#gold-plate)"/>
    <circle class="brand-dot--light" cx="172" cy="845" r="12"/>
    <text class="brand-name brand-name--light" x="172" y="880">Kindle the Moss</text>
  </g>

  <!-- front panel -->
  <g class="front-panel">
    <rect class="white-band" x="45" y="985" width="255" height="132"/>
    <circle class="brand-dot--ink" cx="168" cy="1023" r="16"/>
    <text class="brand-name brand-name--ink" x="168" y="1057">Kindle the Moss</text>
    <text class="product-title" x="168" y="1106">Ultrasonic Essential Oil Aroma Diffuser</text>
    <line class="gold-rule" x1="45" y1="1116" x2="300" y2="1116"/>
    <rect class="pattern-field" x="45" y="1117" width="255" height="230" role="img" aria-label="Cream geometric line pattern"/>
    <ellipse cx="170" cy="1245" rx="72" ry="92" fill="url(#diffuser-tone)" role="img" aria-label="Wood grain teardrop aroma diffuser with teal light ring"/>
  </g>

  <!-- side panel -->
  <g class="side-panel">
    <rect x="300" y="983" width="250" height="364" fill="url(#wood-a)" role="img" aria-label="Warm orange wood grain"/>
    <circle class="brand-dot--light" cx="423" cy="1165" r="15"/>
    <text class="brand-name brand-name--light" x="423" y="1199">Kindle the Moss</text>
  </g>

  <!-- back panel -->
  <g class="back-panel">
    <rect class="white-band" x="550" y="985" width="250" height="132"/>
    <circle class="brand-dot--ink" cx="675" cy="1023" r="16"/>
    <text class="brand-name brand-name--ink" x="675" y="1057">Kindle the Moss</text>
    <text class="product-title" x="675" y="1106">Ultrasonic Essential Oil Aroma Diffuser</text>
    <line class="gold-rule" x1="550" y1="1116" x2="800" y2="1116"/>
    <rect class="pattern-field" x="550" y="1117" width="250" height="230" role="img" aria-label="Cream geometric line pattern"/>
    <ellipse cx="677" cy="1245" rx="72" ry="92" fill="url(#diffuser-tone)" role="img" aria-label="Wood grain teardrop aroma diffuser with teal light ring"/>
  </g>

  <!-- second side panel -->
  <g class="side-panel side-panel--dark">
    <rect x="800" y="983" width="252" height="364" fill="url(#wood-b)" role="img" aria-label="Deep orange wood grain"/>
    <circle class="brand-dot--light" cx="920" cy="1165" r="15"/>
    <text class="brand-name brand-name--light" x="920" y="1199">Kindle the Moss</text>
  </g>
</svg>
</body>
</html>
```